Retail Pricing Subscription Service

Create a compelling a 1-page marketing brochure around a service that allows Pell Worldwide retailers to optimize their retail pricing in their stores. The brochure must be fun, very professionally done, clean, and exciting to want possible clients to want to pick up. See word file for content details. The Pell Global Solutions red and white colors should be used. Also, include relevant photos to liven up the brochure.

Target Market(s)

Pell Toolhouse International Retailers

Requirements
Must have
• See Word file attachment. Should have professionally done photos that are relevant. Get creative!
• Use Pell Toolhouse Global Solutions red and white in the brochure.
• Also, should look like a 'global' service. Maybe add a worldly look to it.
Nice to have
• See Word file
Should not have
• Not cartoon looking. Professional, clean, and exciting look.

```html
<!DOCTYPE html>
<html lang="en">
<head>
<meta charset="utf-8">
<title>Pell Global Solutions – Retail Pricing Strategy</title>
<link rel="stylesheet" href="https://fonts.googleapis.com/css2?family=Ubuntu:ital,wght@0,300;0,400;0,500;0,700;1,400&display=swap">
<style>
  :root{
    --red:#e31b3b;
    --charcoal:#2c2626;
    --white:#ffffff;
    --ink:#333333;
    --stage:#e8e5e0;
  }
  *{margin:0;padding:0;box-sizing:border-box}
  html,body{width:1200px;height:774px;overflow:hidden;background:var(--stage);font-family:"Ubuntu",sans-serif}
  .flyer{position:absolute;left:322px;top:31px;width:696px;height:890px;transform:scale(.8);transform-origin:0 0;background:var(--white);overflow:hidden;box-shadow:0 6px 18px rgba(0,0,0,.25)}
  .layer{position:absolute;left:0;top:0;width:696px;height:890px}
  .brand-name{position:absolute;left:44px;top:70px;font-size:24px;font-weight:500;color:var(--charcoal);line-height:1}
  .title{position:absolute;left:54px;top:166px;font-size:33px;color:var(--white);letter-spacing:.2px;line-height:1}
  .title b{font-weight:700}
  .title span{font-weight:300}
  .intro{position:absolute;left:54px;top:230px;width:586px;color:var(--white)}
  .intro h2{font-size:19px;font-weight:400;margin-bottom:12px}
  .intro h2 em{margin-right:4px}
  .intro p{font-size:9.6px;line-height:13px;text-align:justify;margin-bottom:13px}
  .approach{position:absolute;left:54px;top:448px;width:338px;color:var(--white)}
  .approach h2,.results h2{font-size:23px;line-height:1;margin-bottom:16px}
  .approach h2 b,.results h2 b{font-weight:700}
  .approach h2 span,.results h2 span{font-weight:300}
  .list{list-style:none}
  .list li{position:relative;padding-left:16px;font-size:9.6px;line-height:12.5px;margin-bottom:9px}
  .list li::before{content:"";position:absolute;left:0;top:1px;width:9px;height:9px;border-radius:50%;background:var(--red)}
  .results{position:absolute;left:400px;top:452px;width:250px;height:256px;border:2px solid var(--red);border-radius:9px;background:rgba(215,215,217,.88);padding:18px 16px 0 20px}
  .results h2{color:var(--charcoal)}
  .results h2 b{color:var(--red)}
  .results .list li{font-size:10px;line-height:14px;margin-bottom:8px;color:#222}
  .contact{position:absolute;left:424px;top:758px;font-size:11.5px;line-height:15px;color:var(--ink);font-style:normal}
  .contact h3{font-size:12.5px;font-weight:700;color:var(--red)}
  .contact b{font-weight:700}
</style>
</head>
<body>
<div class="flyer">
  <svg class="layer" viewBox="0 0 696 890" aria-hidden="true">
    <defs>
      <linearGradient id="barFade" x1="0" x2="1">
        <stop offset="0" stop-color="#2c2626"/>
        <stop offset=".55" stop-color="#2c2626" stop-opacity=".95"/>
        <stop offset="1" stop-color="#2c2626" stop-opacity=".35"/>
      </linearGradient>
      <linearGradient id="darkBand" x1="0" y1="0" x2="0" y2="1">
        <stop offset="0" stop-color="#2f2f31"/>
        <stop offset="1" stop-color="#4a4a4c"/>
      </linearGradient>
    </defs>
    <rect x="0" y="420" width="696" height="325" fill="url(#darkBand)"/>
    <rect x="0" y="212" width="696" height="208" fill="var(--red)"/>
    <path d="M0 130 H300 Q318 130 330 145 L342 160 H0 Z" fill="var(--red)"/>
  </svg>

  <svg class="layer" viewBox="0 0 696 890" role="img" aria-label="Photo of a hand moving a chess piece on a chessboard">
    <defs>
      <linearGradient id="chess" x1="0" y1="0" x2="1" y2="1">
        <stop offset="0" stop-color="#d9d4cc"/>
        <stop offset=".5" stop-color="#9fa9b8"/>
        <stop offset="1" stop-color="#6f6a64"/>
      </linearGradient>
    </defs>
    <path d="M398 0 H696 V212 H300 L335 150 Z" fill="url(#chess)"/>
  </svg>

  <svg class="layer" viewBox="0 0 696 890" aria-hidden="true">
    <rect x="0" y="160" width="696" height="52" fill="url(#barFade)"/>
  </svg>

  <svg class="layer" viewBox="0 0 696 890" role="img" aria-label="Photo of planet Earth from space with a sunrise on the horizon">
    <defs>
      <radialGradient id="earth" cx=".75" cy=".45" r=".9">
        <stop offset="0" stop-color="#e8f2ff"/>
        <stop offset=".18" stop-color="#6f93c2"/>
        <stop offset=".55" stop-color="#1f3558"/>
        <stop offset="1" stop-color="#05070d"/>
      </radialGradient>
    </defs>
    <path d="M0 665 H300 Q315 665 322 678 L358 745 L258 890 H0 Z" fill="url(#earth)"/>
    <path d="M0 665 H300 Q315 665 322 678 L358 745" fill="none" stroke="#8a8a8c" stroke-width="2"/>
  </svg>

  <svg class="layer" viewBox="0 0 696 890" aria-hidden="true">
    <path d="M358 745 H696 V890 H258 Z" fill="var(--white)"/>
  </svg>

  <div class="brand-name">Pell Global Solutions</div>

  <h1 class="title"><b>RETAIL</b> <span>PRICING</span> <b>STRATEGY</b></h1>

  <section class="intro">
    <h2><em>GETTING MORE STRATEGIC</em> for Profitable Growth</h2>
    <p>Right now, retail is a battlefield and price remains king. As the top priority for many consumers, your prices must be relevant in order to earn their business. This means pricing that reflects your brand, position in the market, and consumer demand at every moment so you are never priced too high or too low. Price optimization is at the root of the force needed for profit generation in retail. The backbone of retail pricing analytics is science, which is used to price items properly without the need for concessions.</p>
    <p>Pell Global Solutions retail pricing monthly services delivers your business transformational technology, best practices, and expertise needed to excel in today's consumer centric marketplace. We identify margin opportunities to both over and underpricing situations down to the item level. This includes providing you with support in adopt tailored rounding strategies across product offerings, categorizing products into different price strategies, and measure the gross margin impact of our recommended strategies.</p>
  </section>

  <section class="approach">
    <h2><b>Our</b> <span>SERVICE</span> <b>APPROACH</b></h2>
    <ul class="list">
      <li>Understand your long-term pricing vision, pricing image and objectives</li>
      <li>Assess the current state of affairs to your consumer pricing perception</li>
      <li>Gather item-level pricing data one category at a time</li>
      <li>Held in strict confidence, we analyze the data via our proven methodology and return within three days providing insights and suggestions toward improved pricing strategy sorted by highest margin impact</li>
      <li>Implement data-driven suggestions, scorecard results, and inform further</li>
    </ul>
  </section>

  <aside class="results">
    <h2><span>Real</span> <b>RESULTS</b></h2>
    <ul class="list">
      <li>Stop leaving money on the table!</li>
      <li>Higher gross margin dollars</li>
      <li>An enhanced pricing image with your customers</li>
      <li>Drive incremental store traffic</li>
      <li>Create consistency and clean presentation of price</li>
      <li>Making pricing decisions straightforward and quicker - Remove need for manual work</li>
    </ul>
  </aside>

  <address class="contact">
    <h3>Pell Worldwide Holdings</h3>
    1480 Harlow Ct.,<br>
    Maple Ridge, IL, 60599<br>
    T: <b>+1 555.014.2290</b><br>
    F: <b>+1 555.014.7731</b><br>
    www.<b>pellglobalpricinggroup</b>.com
  </address>
</div>
</body>
</html>
```